I need a design for Corvane Homes which is a custom home builder. The name on it will be Dan Hartley, and I will give the phone number to the winning design. No address or website needed.

```html
<!DOCTYPE html>
<html lang="en">
<head>
<meta charset="utf-8">
<title>Corvane Homes – Business Cards</title>
<link href="https://fonts.googleapis.com/css2?family=Jost:wght@300;400;500&display=swap" rel="stylesheet">
<style>
  :root {
    --page-bg: #f7f8fa;
    --card-dark: #221f1f;
    --card-light: #fbfaf6;
    --brand-orange: #f07a22;
    --accent-green: #9bc43a;
    --text-light: #f4f4f4;
    --text-dark: #222222;
    --text-muted-dark: #4a4a4a;
  }
  * { box-sizing: border-box; margin: 0; padding: 0; }
  html, body { width: 1200px; height: 900px; overflow: hidden; }
  body {
    background: var(--page-bg);
    font-family: "Jost", "Futura", sans-serif;
    position: relative;
  }
  .business-card {
    position: absolute;
    width: 540px;
    height: 308px;
    box-shadow: 4px 6px 14px rgba(0,0,0,0.18);
  }
  .business-card--dark { left: 100px; top: 150px; background: var(--card-dark); color: var(--text-light); }
  .business-card--light { left: 560px; top: 450px; background: var(--card-light); color: var(--text-dark); border: 1px solid #d8d8d8; }

  .brand-lockup {
    position: absolute;
    left: 0; right: 0;
    top: 96px;
    text-align: center;
  }
  .brand-name {
    display: inline-flex;
    align-items: center;
    gap: 10px;
    font-weight: 400;
    font-size: 42px;
    line-height: 1;
    color: var(--brand-orange);
    letter-spacing: 0.5px;
  }
  .brand-square {
    width: 16px; height: 16px;
    background: var(--brand-orange);
  }
  .brand-tagline {
    margin-top: 8px;
    font-weight: 400;
    font-size: 15px;
    letter-spacing: 6px;
    text-transform: uppercase;
  }
  .business-card--dark .brand-tagline { color: var(--text-light); }
  .business-card--light .brand-tagline { color: var(--text-muted-dark); }

  .holder-name {
    position: absolute;
    font-weight: 400;
    font-size: 22px;
    letter-spacing: 0.5px;
    text-transform: uppercase;
  }
  .accent-rule {
    position: absolute;
    height: 4px;
    background: var(--accent-green);
  }
  .contact-phone {
    position: absolute;
    display: flex;
    align-items: center;
    gap: 6px;
    font-size: 13px;
    font-weight: 400;
  }
  .contact-phone svg { width: 10px; height: 14px; }

  .business-card--dark .holder-name { left: 34px; bottom: 32px; }
  .business-card--dark .accent-rule { left: 250px; right: 30px; top: 222px; }
  .business-card--dark .contact-phone { left: 370px; top: 234px; color: var(--text-light); }

  .business-card--light .brand-lockup { top: 100px; }
  .business-card--light .holder-name { left: 34px; top: 214px; }
  .business-card--light .accent-rule { left: 218px; right: 40px; top: 230px; }
  .business-card--light .contact-phone { left: 320px; top: 244px; color: var(--text-muted-dark); }
</style>
</head>
<body>

<section class="business-card business-card--dark" aria-label="Business card, dark version">
  <div class="brand-lockup">
    <div class="brand-name"><span class="brand-square"></span>Corvane Homes</div>
    <div class="brand-tagline">Custom Home Builder</div>
  </div>
  <div class="accent-rule"></div>
  <div class="contact-phone">
    <svg viewBox="0 0 10 14" aria-hidden="true"><rect x="0.5" y="0.5" width="9" height="13" rx="1.5" fill="currentColor"/><rect x="2" y="2.5" width="6" height="5" fill="#221f1f"/></svg>
    <span>(555) 014-2276</span>
  </div>
  <div class="holder-name">Dan Hartley</div>
</section>

<section class="business-card business-card--light" aria-label="Business card, light version">
  <div class="brand-lockup">
    <div class="brand-name"><span class="brand-square"></span>Corvane Homes</div>
    <div class="brand-tagline">Custom Home Builder</div>
  </div>
  <div class="holder-name">Dan Hartley</div>
  <div class="accent-rule"></div>
  <div class="contact-phone">
    <svg viewBox="0 0 10 14" aria-hidden="true"><rect x="0.5" y="0.5" width="9" height="13" rx="1.5" fill="currentColor"/><rect x="2" y="2.5" width="6" height="5" fill="#fbfaf6"/></svg>
    <span>(555) 014-2276</span>
  </div>
</section>

</body>
</html>
```